Business Card Design Project

Hello
I want a Simple Business card that uses the company logo that is easily reasonable but looks professional as I am an IT Services company and would look to share these cards with prospective clients.
The details are:
Kelvo Ridge Solutions
14 Marlow Crescent
Birmingham
B7 4QT
Telephone 0845 271 6049
I would like my name Gareth Wilcombe and my title Director on the card.
Target Market(s)
IT Professionals
Industry/Entity Type
Business

```html
<!DOCTYPE html>
<html lang="en">
<head>
<meta charset="utf-8">
<title>Kelvo Ridge Solutions – Business Card</title>
<link href="https://fonts.googleapis.com/css2?family=Oswald:wght@500;600&display=swap" rel="stylesheet">
<style>
  :root {
    --backdrop: #2b2b2b;
    --card: #ffffff;
    --band-green: #9dcc4f;
    --band-yellow: #ffd966;
    --band-lime: #c6df6b;
    --band-pale: #e4eb6c;
    --ink: #231f20;
    --ink-light: #ffffff;
    --accent: #8cc63f;
  }
  html, body {
    margin: 0;
    width: 1200px;
    height: 900px;
    overflow: hidden;
    background: var(--backdrop);
  }
  .business-card {
    position: absolute;
    left: 421px;
    top: 162px;
    width: 322px;
    height: 578px;
    background: var(--card);
    box-shadow: 0 4px 14px rgba(0,0,0,0.45);
  }
  .business-card svg { display: block; }
  .card-text {
    font-family: 'Oswald', 'Arial Narrow', sans-serif;
    font-weight: 600;
    fill: var(--ink-light);
  }
  .wordmark {
    font-family: 'Oswald', 'Arial Narrow', sans-serif;
    font-weight: 600;
    fill: var(--ink);
  }
  .band-green { fill: var(--band-green); }
  .band-yellow { fill: var(--band-yellow); }
  .band-lime { fill: var(--band-lime); }
  .band-pale { fill: var(--band-pale); }
  .wordmark-dot { fill: var(--accent); }
</style>
</head>
<body>
  <div class="business-card">
    <svg width="322" height="578" viewBox="0 0 322 578" xmlns="http://www.w3.org/2000/svg">
      <!-- name ribbons -->
      <polygon class="band-yellow" points="25,178 322,80 322,121 25,219"/>
      <polygon class="band-green" points="0,108 322,0 322,78 0,186"/>
      <text class="card-text" x="180" y="97" font-size="27" text-anchor="middle" transform="rotate(-18.5 180 87)">Gareth Wilcombe</text>
      <text class="card-text" x="250" y="134" font-size="22" text-anchor="middle" transform="rotate(-18.5 250 126)">Director</text>

      <!-- company name -->
      <circle class="wordmark-dot" cx="22" cy="300" r="9"/>
      <text class="wordmark" x="168" y="311" font-size="28" text-anchor="middle">Kelvo Ridge Solutions</text>

      <!-- contact ribbons -->
      <polygon class="band-lime" points="0,371 322,468 322,518 0,421"/>
      <polygon class="band-pale" points="0,421 193,479 193,515 0,457"/>
      <text class="card-text" x="150" y="446" font-size="24" text-anchor="middle" transform="rotate(16.8 150 438)">Birmingham B7 4QT</text>
      <text class="card-text" x="86" y="472" font-size="18" text-anchor="middle" transform="rotate(16.8 86 466)">0845 271 6049</text>
    </svg>
  </div>
</body>
</html>
```